Bref créative
KorvaLyne Stationary
Dennis Traven's cards
Professional
Dennis Traven, PhD, JD, MBA, MPM
Owner/Senior Consultant
PO Box 862
587E Harwick Rd
Hollenbrook, NQ 53418-4471
dtraven@korvalyne-consulting.example
www.korvalyne-consulting.example
Finding clear paths through your learning challenges. Jointly.
KorvaLyne-Consulting, LLC is proud to be a member of:
Gerald K Venn, Venn's consortium
Continental Guild of Learning Advisors and Presenters

```html
<!DOCTYPE html>
<html lang="en">
<head>
<meta charset="utf-8">
<title>KorvaLyne Consulting – Business Card</title>
<link rel="stylesheet" href="https://fonts.googleapis.com/css2?family=Open+Sans:wght@400;600;700;800&display=swap">
<style>
  :root {
    --page-bg: #e9e7e4;
    --card-bg: #ffffff;
    --brand-blue: #1d5f86;
    --brand-blue-dark: #0e3f5c;
    --ink: #3a3d40;
    --ink-soft: #5b5f63;
    --steel-light: #d7d9dc;
    --steel-dark: #7d8186;
  }
  html, body {
    margin: 0;
    padding: 0;
    width: 1200px;
    height: 914px;
    overflow: hidden;
    background: var(--page-bg);
    font-family: "Open Sans", Arial, sans-serif;
  }
  .card {
    position: absolute;
    left: 100px;
    top: 171px;
    width: 1000px;
    height: 572px;
    background: var(--card-bg);
    box-shadow: 0 10px 30px rgba(0,0,0,0.18);
    overflow: hidden;
  }
  .brand {
    position: absolute;
    left: 0;
    right: 0;
    top: 52px;
    text-align: center;
  }
  .brand-dot {
    width: 132px;
    height: 132px;
    margin: 0 auto;
    border-radius: 50%;
    background: var(--brand-blue);
  }
  .brand-name {
    margin-top: 18px;
    font-size: 54px;
    font-weight: 800;
    letter-spacing: -0.5px;
    color: var(--ink);
    line-height: 1;
  }
  .brand-tagline {
    margin-top: 8px;
    font-size: 15px;
    color: var(--brand-blue);
    letter-spacing: 0.3px;
  }
  .contact-person {
    position: absolute;
    right: 520px;
    top: 318px;
    text-align: right;
    color: var(--ink-soft);
    font-size: 17px;
    line-height: 1.5;
  }
  .person-name {
    font-size: 22px;
    font-weight: 700;
    color: var(--brand-blue);
  }
  .person-title { margin-bottom: 14px; }
  .divider {
    position: absolute;
    left: 500px;
    top: 318px;
    width: 1px;
    height: 140px;
    background: var(--steel-dark);
  }
  .contact-lines {
    position: absolute;
    left: 516px;
    top: 318px;
    list-style: none;
    margin: 0;
    padding: 0;
    color: var(--ink-soft);
    font-size: 16px;
    line-height: 27px;
  }
  .contact-lines li { display: flex; align-items: center; gap: 8px; }
  .contact-lines svg { width: 16px; height: 16px; flex: none; }
  .card-bands {
    position: absolute;
    left: 0;
    bottom: 0;
    width: 1000px;
    height: 110px;
  }
</style>
</head>
<body>
  <div class="card">
    <div class="brand">
      <div class="brand-dot"></div>
      <div class="brand-name">KorvaLyne-Consulting</div>
      <div class="brand-tagline">Finding clear paths through your learning challenges. Jointly.</div>
    </div>

    <div class="contact-person">
      <div class="person-name">Dennis Traven, PhD, JD, MBA, MPM</div>
      <div class="person-title">Owner/Senior Consultant</div>
      <div>PO Box 862 · 587E Harwick Rd</div>
      <div>Hollenbrook, NQ 53418-4471</div>
    </div>

    <div class="divider"></div>

    <ul class="contact-lines">
      <li><svg viewBox="0 0 16 16"><circle cx="8" cy="8" r="8" fill="var(--brand-blue)"/><path d="M5 4.5l1.6-.4 1 2-1 .8a5 5 0 0 0 2.5 2.5l.8-1 2 1-.4 1.6c-3.6.3-6.8-2.9-6.5-6.5z" fill="#fff"/></svg>555-010-4821</li>
      <li><svg viewBox="0 0 16 16"><circle cx="8" cy="8" r="8" fill="var(--brand-blue)"/><rect x="5" y="3.5" width="6" height="9" rx="1" fill="#fff"/></svg>555-010-3397</li>
      <li><svg viewBox="0 0 16 16"><circle cx="8" cy="8" r="8" fill="var(--brand-blue)"/><rect x="4" y="6" width="8" height="5" fill="#fff"/><rect x="5.5" y="3.5" width="5" height="3" fill="#fff"/></svg>555-010-7604</li>
      <li><svg viewBox="0 0 16 16"><circle cx="8" cy="8" r="8" fill="var(--brand-blue)"/><rect x="4" y="5" width="8" height="6" fill="#fff"/><path d="M4 5l4 3.5L12 5" stroke="var(--brand-blue)" fill="none"/></svg>dtraven@korvalyne-consulting.example</li>
      <li><svg viewBox="0 0 16 16"><circle cx="8" cy="8" r="8" fill="var(--brand-blue)"/><circle cx="8" cy="8" r="4" fill="none" stroke="#fff" stroke-width="1.3"/><path d="M4 8h8M8 4v8" stroke="#fff" stroke-width="1"/></svg>www.korvalyne-consulting.example</li>
    </ul>

    <svg class="card-bands" viewBox="0 0 1000 110" aria-hidden="true">
      <defs>
        <linearGradient id="band-blue" x1="0" x2="1" y1="0" y2="0">
          <stop offset="0" stop-color="var(--brand-blue-dark)"/>
          <stop offset="1" stop-color="var(--brand-blue)"/>
        </linearGradient>
        <linearGradient id="band-steel" x1="0" x2="0" y1="0" y2="1">
          <stop offset="0" stop-color="var(--steel-light)"/>
          <stop offset="0.5" stop-color="#ffffff"/>
          <stop offset="1" stop-color="var(--steel-dark)"/>
        </linearGradient>
      </defs>
      <polygon points="0,18 560,18 600,58 0,58" fill="url(#band-blue)"/>
      <polygon points="590,58 1000,58 1000,96 630,96" fill="url(#band-steel)"/>
    </svg>
  </div>
</body>
</html>
```